Marguerite's Stone Hearth Trattoria Pitch Deck

Clean and Minimalist Layout: Use a clean and uncluttered layout with ample white space to enhance readability and focus on the key content.

Color Palette: Choose a color scheme that aligns with your brand identity. Black and White. Opt for a combination of complementary colors to create a visually appealing and cohesive look throughout the presentation.

Typography: Select modern and legible fonts for headings and body text. Consider using a combination of serif and sans-serif fonts to create contrast and hierarchy.

High-Quality Images: Incorporate high-resolution images that visually represent your pizzeria, food offerings, and brand. Ensure the images are clear, well-lit, and of professional quality.

Graphs and Charts: Utilize visually appealing graphs and charts to present financial projections, market data, and growth metrics. Choose appropriate chart types, such as bar graphs or line charts, to effectively communicate data.

Iconography: Include relevant icons and symbols to enhance visual interest and provide quick visual cues. Use them to represent different sections, services, or key points in your presentation.

Slide Transitions and Animations: Use subtle slide transitions and animations to add a touch of interactivity and engage your audience. However, avoid overusing flashy animations that may distract from the content.

Consistent Branding: Ensure that your pitch deck maintains consistent branding elements throughout, such as your logo, color scheme, and typography. This helps to reinforce your brand identity and create a cohesive presentation.

Remember, the goal is to create a visually appealing and professional pitch deck that effectively communicates your key messages. Use visuals, graphs, and design elements strategically to enhance understanding and engagement with your audience.

Target Market(s)

Investors

Industry/Entity Type

Food Industry

Font styles to use
Serif

Colors

Designer to choose only greyscale colors for use in the design.

Requirements
Must have
• Modern and Professional Look: Opt for a modern design that reflects the professional nature of your business. Use clean lines, contemporary fonts, and a visually appealing color scheme to create a polished and professional appearance. Consistent Branding: Incorporate your pizzeria's branding elements such as the logo, colors, and typography throughout the pitch deck. Consistency in branding helps to establish a cohesive and memorable visual identity. Visual Hierarchy: Use visual hierarchy to guide the viewer's attention and emphasize important information. Utilize font sizes, colors, and formatting techniques such as bold and italics to differentiate headings, subheadings, and body text. Engaging Visuals: Incorporate relevant and eye-catching visuals such as high-quality images, graphics, and icons. Visuals should support your content and help communicate your message effectively. Well-Structured Layout: Organize your content into sections and use clear headings and subheadings to create a logical flow. Ensure that each slide has enough white space for readability and avoid cluttered designs. Legible Fonts: Choose fonts that are easy to read on both computer screens and projection screens. Stick to a maximum of two font styles to maintain a clean and professional look. Charts and Graphs: When presenting data or statistics, use charts, graphs, and infographics to present information visually. This makes complex information more digestible and visually appealing. Slide Transitions and Animations: Use slide transitions and subtle animations to enhance the visual experience. However, avoid excessive animations that can distract from your content. Balance of Text and Visuals: Strike a balance between text and visuals. Avoid overcrowding slides with excessive text and focus on presenting key points in a concise and visually appealing manner. Relevance to Content: Ensure that the design elements align with and enhance the content of your pitch deck. Avoid using decorative elements that do not serve a purpose or distract from the main message. Remember, the design should complement and support your content rather than overpowering it. A well-designed pitch deck will capture attention, convey professionalism, and enhance the overall impact of your presentation.

```html
<!DOCTYPE html>
<html lang="en">
<head>
<meta charset="utf-8">
<title>Marguerite's Stone Hearth Trattoria – Pitch Deck</title>
<link rel="stylesheet" href="https://fonts.googleapis.com/css2?family=DM+Serif+Display&family=DM+Sans:wght@400;700&display=swap">
<style>
:root{
  --ink:#000;
  --paper:#fff;
  --sheet:#fff;
  --muted:#333;
  --rule:#9a9a9a;
  --shadow:rgba(0,0,0,.28);
}
*{margin:0;padding:0;box-sizing:border-box}
html,body{width:1200px;height:2194px;overflow:hidden;background:var(--sheet)}
body{position:relative;font-family:"DM Sans",Arial,sans-serif;color:var(--ink)}
.slide{position:absolute;width:542px;height:304px;background:var(--paper);overflow:hidden;box-shadow:8px 10px 26px var(--shadow)}
.col-left{left:39px}.col-right{left:618px}
.abs{position:absolute}
.photo{position:absolute}
.band{position:absolute;background:var(--ink)}
.serif{font-family:"DM Serif Display",Georgia,serif;font-weight:400}
.brand{position:absolute;font-family:"DM Serif Display",Georgia,serif;font-size:15px;line-height:1;color:var(--ink);white-space:nowrap}
.brand.light{color:var(--paper)}
.title{position:absolute;font-family:"DM Serif Display",Georgia,serif;font-size:22px;line-height:1.2;color:var(--ink)}
.kicker{position:absolute;font-family:"DM Serif Display",Georgia,serif;font-size:7.5px;color:var(--ink)}
.body{position:absolute;font-size:6.3px;line-height:1.85;color:var(--muted);text-align:justify}
.body b{color:var(--ink)}
.body p+p{margin-top:9px}
.body.tight{line-height:1.4;text-align:left}
.pagenum{position:absolute;font-size:6px;color:var(--paper)}
.pagenum.dark{color:var(--ink)}
.url{position:absolute;writing-mode:vertical-rl;transform:rotate(180deg);font-size:6px;color:var(--paper);letter-spacing:.1px}
.url.dark{color:var(--ink)}
.vrule{position:absolute;width:.6px;background:var(--rule)}
</style>
</head>
<body>

<!-- 1 Cover -->
<section class="slide col-left" style="top:74px;background:#2b2018">
  <div class="photo" role="img" aria-label="Dim brick oven with a pizza in front" style="inset:0;background:radial-gradient(ellipse at 50% 25%,#6e5530 0%,#3a2b1c 45%,#1e1610 100%)"></div>
  <div class="brand light" style="left:52px;top:132px;font-size:34px">Marguerite's</div>
  <div class="abs" style="left:160px;top:176px;width:14px;height:14px;border:1.5px solid var(--paper);border-radius:50%"></div>
  <h1 class="serif abs" style="left:314px;top:86px;font-size:25px;line-height:1.28;color:var(--paper)">Pitchdeck<br>presentation</h1>
  <div class="abs" style="left:314px;top:160px;width:207px;height:.6px;background:#8a7a66"></div>
  <div class="abs" style="left:314px;top:168px;font-size:8.6px;line-height:1.45;color:var(--paper)">
    <div class="serif">Paolo Ferraro (Owner &amp; CEO):</div>
    <div>paolo@margueritestrattoria.com</div>
    <div class="serif">Marcus Lindell (Owner, Silent Partner):</div>
    <div>marcus@margueritestrattoria.com</div>
  </div>
  <div class="pagenum" style="left:524px;top:20px;color:#8a7a66">1</div>
  <div class="url" style="left:521px;top:200px;color:#6d5f4f">www.margueritestrattoria.com</div>
</section>

<!-- 2 Introduction -->
<section class="slide col-right" style="top:319px">
  <div class="brand" style="left:33px;top:22px">Marguerite's</div>
  <h2 class="title" style="left:36px;top:82px">Introduction</h2>
  <div class="body" style="left:36px;top:120px;width:198px">
    <p><b>Marguerite's Stone Hearth Trattoria</b> is a quality casual restaurant offering freshly cooked, delicious pizzas made with carefully crafted homemade sauce and dough. We prioritize customer satisfaction and provide lightning-quick food times, making us a top choice for takeout and delivery.</p>
    <p><b>Vision and Mission Statement:</b> Our vision is to become the go-to destination for exceptional pizza experiences, known for our quality ingredients and outstanding service. Our mission is to delight customers with every bite and create memorable moments through our delicious pizzas.</p>
  </div>
  <div class="photo" role="img" aria-label="Two owners standing behind a table of pizzas in front of a brick oven" style="left:255px;top:33px;width:238px;height:238px;border-radius:50%;background:radial-gradient(circle at 50% 40%,#a89a8a 0%,#6f655b 55%,#3b352f 100%)"></div>
  <svg class="abs" style="left:250px;top:28px" width="248" height="248" viewBox="0 0 248 248" aria-hidden="true"><circle cx="124" cy="124" r="121" fill="none" stroke="#1a1a1a" stroke-width="3"/></svg>
  <div class="band" style="left:506px;top:0;width:36px;height:304px"></div>
  <div class="pagenum" style="left:522px;top:20px">2</div>
  <div class="url" style="left:520px;top:200px">www.margueritestrattoria.com</div>
</section>

<!-- 3 Market Opportunity divider -->
<section class="slide col-left" style="top:565px">
  <div class="band" style="left:0;top:0;width:100px;height:304px"></div>
  <div class="pagenum" style="left:16px;top:20px">3</div>
  <div class="vrule" style="left:18px;top:33px;height:150px;background:#777"></div>
  <div class="url" style="left:15px;top:200px">www.margueritestrattoria.com</div>
  <div class="photo" role="img" aria-label="Cheese pizza on a peel in front of the oven fire" style="left:45px;top:17px;width:135px;height:287px;background:linear-gradient(180deg,#e6a040 0%,#b85a1c 30%,#d98a32 60%,#8a4a20 100%)"></div>
  <div class="photo" role="img" aria-label="Hands shaping dough balls on a floured table" style="left:191px;top:17px;width:123px;height:106px;background:linear-gradient(160deg,#f2efe9 0%,#d8d2c7 60%,#bdb5a8 100%)"></div>
  <div class="photo" role="img" aria-label="Guests sharing slices of topped pizza" style="left:191px;top:132px;width:123px;height:172px;background:linear-gradient(170deg,#5e5a4e 0%,#9b6b4e 50%,#c48a5c 100%)"></div>
  <div class="brand" style="left:355px;top:92px;font-size:24px">Marguerite's</div>
  <h2 class="title" style="left:352px;top:178px;font-size:26px;line-height:1.25">The Market<br>Opportunity</h2>
</section>

<!-- 4 Industry overview -->
<section class="slide col-right" style="top:810px">
  <div class="photo" role="img" aria-label="Family laughing while eating pizza together" style="left:0;top:0;width:262px;height:240px;background:linear-gradient(135deg,#8a8680 0%,#b59a85 45%,#6a6560 100%)"></div>
  <div class="photo" role="img" aria-label="Grandfather and grandchild eating pizza slices from a box" style="left:121px;top:43px;width:141px;height:261px;border:5px solid var(--paper);border-right:0;border-bottom:0;background:linear-gradient(160deg,#c9c3ba 0%,#b08a6a 55%,#d6b88e 100%)"></div>
  <div class="band" style="left:0;top:250px;width:116px;height:54px"></div>
  <div class="brand light" style="left:22px;top:270px">Marguerite's</div>
  <div class="kicker" style="left:317px;top:73px">The Market Opportunity</div>
  <h2 class="title" style="left:317px;top:86px">Overview of<br>the Pizza<br>Industry:</h2>
  <div class="body" style="left:317px;top:174px;width:140px">The pizza industry is a thriving and highly popular segment of the food service market. With a diverse range of customers and a growing demand for convenient dining options, the pizza industry presents significant growth opportunities.</div>
  <div class="band" style="left:506px;top:0;width:36px;height:304px"></div>
  <div class="pagenum" style="left:522px;top:20px">4</div>
  <div class="url" style="left:520px;top:200px">www.margueritestrattoria.com</div>
</section>

<!-- 5 Market size -->
<section class="slide col-left" style="top:1055px">
  <div class="band" style="left:0;top:0;width:109px;height:304px"></div>
  <div class="pagenum" style="left:16px;top:20px">5</div>
  <div class="vrule" style="left:18px;top:33px;height:150px;background:#777"></div>
  <div class="url" style="left:15px;top:200px">www.margueritestrattoria.com</div>
  <div class="photo" role="img" aria-label="Chef lifting a large cheese pizza from the oven on a peel" style="left:45px;top:28px;width:263px;height:248px;background:linear-gradient(150deg,#d9d6d0 0%,#a9a39a 25%,#e0a048 50%,#c46a26 75%,#8a8178 100%)"></div>
  <div class="brand" style="left:461px;top:15px">Marguerite's</div>
  <div class="kicker" style="left:341px;top:73px">The Market Opportunity</div>
  <h2 class="title" style="left:341px;top:86px">Market Size<br>and Growth<br>Potential:</h2>
  <div class="body" style="left:341px;top:174px;width:140px">The pizza industry generates billions of dollars in revenue each year, and its potential for growth remains strong. As we expand our presence, we tap into the market's appetite for quality pizza options and capitalize on the increasing trend of takeout and delivery services.</div>
</section>

<!-- 6 Target audience -->
<section class="slide col-right" style="top:1301px">
  <div class="band" style="left:320px;top:0;width:222px;height:304px"></div>
  <div class="brand light" style="left:460px;top:17px">Marguerite's</div>
  <div class="photo" role="img" aria-label="Group of friends laughing over pizza at a table" style="left:251px;top:53px;width:171px;height:198px;background:linear-gradient(140deg,#e8e6e2 0%,#8e9db0 45%,#c9a27a 100%)"></div>
  <div class="photo" role="img" aria-label="Two friends enjoying pizza slices" style="left:427px;top:53px;width:115px;height:198px;background:linear-gradient(160deg,#ecebe8 0%,#7d8ca0 55%,#b8946c 100%)"></div>
  <div class="pagenum dark" style="left:16px;top:20px">6</div>
  <div class="vrule" style="left:18px;top:33px;height:150px"></div>
  <div class="url dark" style="left:15px;top:200px">www.margueritestrattoria.com</div>
  <div class="kicker" style="left:48px;top:64px">The Market Opportunity</div>
  <h2 class="title" style="left:48px;top:77px">Target Audience<br>and Customer<br>Demographics</h2>
  <div class="body" style="left:48px;top:172px;width:168px">Our target audience encompasses a wide range of individuals from 18 to 80 years old, both male and female, with a focus on the middle-class demographic. By offering a menu that caters to diverse tastes and preferences, we can attract a broad customer base.</div>
</section>

<!-- 7 USP -->
<section class="slide col-left" style="top:1546px">
  <div class="band" style="left:0;top:0;width:410px;height:304px"></div>
  <div class="brand" style="left:461px;top:15px">Marguerite's</div>
  <div class="photo" role="img" aria-label="Cheese pizza baking on the oven floor beside the flames" style="left:251px;top:55px;width:291px;height:193px;background:linear-gradient(165deg,#f0b050 0%,#6a4a30 28%,#d07a30 55%,#8a8580 100%)"></div>
  <div class="pagenum" style="left:16px;top:20px">7</div>
  <div class="vrule" style="left:18px;top:33px;height:150px;background:#777"></div>
  <div class="url" style="left:15px;top:200px">www.margueritestrattoria.com</div>
  <h2 class="title" style="left:50px;top:40px;color:var(--paper);line-height:1.22">Unique Selling<br>Proposition</h2>
  <div class="body tight" style="left:50px;top:104px;width:165px;color:var(--paper)">
    <p><b style="color:var(--paper)">What Sets Our Pizzeria Apart:</b><br>At Marguerite's Stone Hearth Trattoria, our commitment to excellence sets us apart. We pride ourselves on using carefully crafted proprietary recipes for our homemade sauce and dough, resulting in exceptional product quality. Our small, profitable menu ensures consistency and allows us to deliver lightning-quick food times, making us a customer favorite.</p>
    <p><b style="color:var(--paper)">Key Differentiators and Competitive Advantages:</b><br>Our ability to make anything on our menu in a matter of minutes, coupled with our convenient ordering options, including mobile ordering, delivery service, takeout, and in-person dining, sets us apart from the competition. We prioritize meeting our customers' exact fast-paced needs and providing the best quality product and service.</p>
  </div>
</section>

<!-- 8 Business model -->
<section class="slide col-right" style="top:1790px">
  <div class="photo" role="img" aria-label="Hands dusting flour on a work table" style="left:0;top:0;width:85px;height:104px;background:linear-gradient(160deg,#f4f2ee 0%,#d9d3c9 100%)"></div>
  <div class="photo" role="img" aria-label="Scale and mixing bowl on a prep counter" style="left:93px;top:0;width:158px;height:104px;background:linear-gradient(160deg,#e9e7e3 0%,#9a9690 50%,#d4cfc6 100%)"></div>
  <div class="photo" role="img" aria-label="Rolling pin and dough balls on a floured table" style="left:0;top:112px;width:251px;height:192px;background:linear-gradient(170deg,#eeeae3 0%,#d8cfbf 55%,#b9ad98 100%)"></div>
  <div class="band" style="left:0;top:265px;width:116px;height:39px"></div>
  <div class="brand light" style="left:22px;top:278px">Marguerite's</div>
  <h2 class="title" style="left:282px;top:42px;font-size:21px">Business Model</h2>
  <div class="body tight" style="left:282px;top:82px;width:205px;font-size:6.2px">
    <p><b>Revenue Streams:</b><br>Our revenue streams include dine-in, takeout, delivery, and catering services. By offering multiple avenues for customers to enjoy our pizzas, we maximize revenue opportunities and cater to various preferences.</p>
    <p style="margin-top:22px"><b>Pricing Strategy and Menu Overview:</b><br>We have meticulously priced our menu to ensure maximum profitability while delivering value to our customers. Our menu offers a carefully selected range of signature pies, including the Hearth, Rustica, and Classic pies, ensuring that each pizza is a delightful experience for our customers.</p>
    <p style="margin-top:22px"><b>Operating Hours and Location(s):</b><br>Our pizzeria operates from 11 am to 9 pm, allowing us to cater to lunch and dinner crowds. Our flagship location is situated at 214 Harbor Road, Building 2, Unit 7, Millbrook, DE 19960, providing a convenient and accessible location for customers.</p>
  </div>
  <div class="band" style="left:506px;top:0;width:36px;height:304px"></div>
  <div class="pagenum" style="left:522px;top:20px">8</div>
  <div class="url" style="left:520px;top:200px">www.margueritestrattoria.com</div>
</section>

</body>
</html>
```